Entrepreneur needs a business card design

I need a business card to name my three companies, as well as contact information.
I'm open on design and color and it can be plain or complex. I'm open on colors but I think I prefer something somewhat formal but fun as well.
I'm open on whether the background is plain or has design in it. I don't have company logos.
Target Market(s)
Auto dealers, realtors and property managers
Industry/Entity Type
Business
Contact Information for Business Card
HALVERSEN FAMILY PROPERTIES, LLC
HALVERSEN PUBLISHING, LLC
MOTORVANE CONSULTING, LLC
Lee Halversen
2871 W. Tamarind Ave. #419
Boise, Idaho 83719-2056
208-514-3092
lee@halv3rn.com

```html
<!DOCTYPE html>
<html lang="en">
<head>
<meta charset="utf-8">
<title>Lee Halversen – Business Card</title>
<link rel="stylesheet" href="https://fonts.googleapis.com/css2?family=Questrial&family=Poppins:wght@600&display=swap">
<style>
  :root {
    --page-bg: #ecebe8;
    --card-white: #ffffff;
    --band-orange: #e0632b;
    --band-rust: #c24c25;
    --band-brick: #9c3a1f;
    --name-orange: #e2642a;
    --contact-grey: #5a5a5a;
  }
  html, body {
    margin: 0;
    width: 1200px;
    height: 1000px;
    overflow: hidden;
    background: var(--page-bg);
  }
  .canvas {
    width: 1200px;
    height: 1000px;
    display: block;
  }
  .card-surface { fill: var(--card-white); }
  .band-primary { fill: var(--band-orange); }
  .band-secondary { fill: var(--band-rust); }
  .band-tertiary { fill: var(--band-brick); }
  .company-name {
    font-family: "Questrial", "Century Gothic", sans-serif;
    font-size: 22px;
    fill: var(--card-white);
    letter-spacing: 0.3px;
  }
  .person-name {
    font-family: "Poppins", "Century Gothic", sans-serif;
    font-weight: 600;
    font-size: 42px;
    fill: var(--name-orange);
  }
  .contact-line {
    font-family: "Questrial", "Century Gothic", sans-serif;
    font-size: 26px;
    fill: var(--contact-grey);
  }
</style>
</head>
<body>
<svg class="canvas" viewBox="0 0 1200 1000" xmlns="http://www.w3.org/2000/svg" aria-label="Business card for Lee Halversen">
  <defs>
    <clipPath id="card-shape">
      <rect x="0" y="0" width="1000" height="570" rx="28" ry="28"/>
    </clipPath>
    <filter id="card-lift" x="-10%" y="-10%" width="120%" height="130%">
      <feDropShadow dx="0" dy="8" stdDeviation="12" flood-color="#000" flood-opacity="0.18"/>
    </filter>
  </defs>

  <g class="business-card" transform="translate(100 215)">
    <rect class="card-surface" x="0" y="0" width="1000" height="570" rx="28" ry="28" filter="url(#card-lift)"/>

    <g class="company-bands" clip-path="url(#card-shape)">
      <polygon class="band-primary" points="380,0 1000,0 1000,215 530,215"/>
      <polygon class="band-secondary" points="537,225 1000,225 1000,290 583,290"/>
      <polygon class="band-tertiary" points="590,300 1000,300 1000,365 635,365"/>
    </g>

    <g class="company-list" clip-path="url(#card-shape)">
      <text class="company-name" x="542" y="198">HALVERSEN FAMILY PROPERTIES, LLC</text>
      <text class="company-name" x="590" y="267">HALVERSEN PUBLISHING, LLC</text>
      <text class="company-name" x="640" y="342">MOTORVANE CONSULTING, LLC</text>
    </g>

    <g class="contact-block">
      <text class="person-name" x="945" y="445" text-anchor="end">Lee Halversen</text>
      <text class="contact-line" x="945" y="493" text-anchor="end">2871 W. Tamarind Ave. #419 Boise, Idaho 83719-2056</text>
      <text class="contact-line" x="945" y="533" text-anchor="end">208-514-3092 lee@halv3rn.com</text>
    </g>
  </g>
</svg>
</body>
</html>
```